Printing Company needs Website

PLEASE REVIEW ALL IMAGES, I HAVE INCLUDED A WEBSITE MOCKUP IDEA AND LOGO FILES IN THESE IMAGES.

Vexo-Marks Provides printing services to multiple businesses. We Focus on 4 main markets. Signage (Signs, Banners, Wraps, Custom graphics), Printing (flyers, brochures, business cards, Postcards), Apparel (printed shirts, hoodies, sweatshirts), Promotional Products (mugs, golf balls, brimo cans, pens), We try to sell ourselves on total brand imaging, our slogan is "Print Anything." because we want to be able to provide any type of printing to our customers. Consumer targeting should be targeted towards small business, and wholesale targeting should be geared toward, merchandising, branding, marketing, design, signage, apparel, embroidery, and printing groups. WE DO OFFER DESIGN SERVICES, I have attached one lindmoor council logo design as an example.

I need a website designed both for wholesale and consumer based people. Wholesale customers would have their own login and consumers would also have their own.
I need there to be an online designer software (possibly java) built in so that the customer can order their product or upload their artwork online to see the proof for approval. There will need to be an commence setup, and I do have a quillo account if that helps. Shipping must be auto calculated at the time of ordering. I would Like to make it to where when customer orders a product if it is outside of the dimensions requested on the site that the customer is warned of clipping or skewing.

I will be working closely aside the designer I pick to aid in the uploading and configuration of pricing structure, weight, and imagery if selected. This will be a lengthy project, and I will be willing to pay for the additional help so long as you are completely aware of the needs, Happy designing!!
Updates

I love all of the designs so far everyone! I will be reviewing PLEASE NOTE, IF I APPROVE YOUR WEB DESIGN, I WILL WANT YOU TO COMPLETE THE ENTIRE DESIGN INCLUDING A DESIGN PROOFING SETUP FOR MY CUSTOMERS INTEGRATED IN AS I HAVE STATED IN THE ORIGINAL STATEMENT. PLEASE ASK QUESTIONS IF YOU DON'T UNDERSTAND!

Target Market(s)

Small Business, School Athletics, Merchandising groups, Branding Groups, Larger Printers, Sign makers, Embroidery shops, Screen Printing Shops

Industry/Entity Type

It Company

Font styles to use
Sans Serif

Colors
000000
1b1b1b
757575
ec1f27

Requirements
Must have
• Built in design setup to each product with sizing, Ability to add pre-designed templates, .pdf print ready files after upload, Wholesale account, or Business accounts all with different pricing structures, Must be willing to aid in setup of all products and services (willing pay additional for setup costs.)
Nice to have
• SEO Optimization, targeting specific groups listed, automatic ordering to outsource vendors straight from site listing drop ship location if need be.

```html
<!DOCTYPE html>
<html lang="en">
<head>
<meta charset="utf-8">
<title>Vexo-Marks — Print Anything</title>
<link href="https://fonts.googleapis.com/css2?family=Montserrat:ital,wght@0,500;0,600;0,700;1,700;1,800&family=Open+Sans:wght@400;600&display=swap" rel="stylesheet">
<style>
  :root {
    --black: #000000;
    --charcoal: #1b1b1b;
    --grey: #757575;
    --red: #ec1f27;
    --white: #ffffff;
    --link-grey: #b4b4b4;
  }
  * { margin: 0; padding: 0; box-sizing: border-box; }
  html, body { width: 1200px; height: 1037px; overflow: hidden; background: var(--charcoal); }
  body { position: relative; font-family: "Open Sans", Arial, sans-serif; }

  .site-header { position: absolute; left: 0; top: 0; width: 1200px; height: 152px; background: var(--charcoal); }
  .brand { position: absolute; left: 0; top: 44px; width: 1200px; display: flex; flex-direction: column; align-items: center; }
  .brand-row { display: flex; align-items: center; gap: 10px; }
  .brand-dot { width: 18px; height: 18px; border-radius: 50%; background: var(--red); }
  .brand-name { font-family: "Montserrat", Arial, sans-serif; font-weight: 700; font-size: 36px; color: var(--white); letter-spacing: 0.5px; }
  .brand-tagline { margin-top: 4px; margin-left: 120px; font-size: 10px; color: var(--white); }

  .main-nav { position: absolute; left: 0; top: 152px; width: 1200px; height: 64px; background: var(--red); }
  .nav-active { position: absolute; left: 112px; top: 0; width: 107px; height: 61px; background: var(--charcoal); }
  .nav-item { position: absolute; top: 0; height: 61px; line-height: 61px; transform: translateX(-50%);
    font-family: "Montserrat", Arial, sans-serif; font-weight: 600; font-size: 13px; color: var(--white); white-space: nowrap; }
  .nav-item.is-current { color: var(--red); }

  .hero { position: absolute; left: 0; top: 216px; width: 1200px; height: 465px;
    background: linear-gradient(180deg, #8fb0d4 0%, #c9d7e6 22%, #6f7a4c 30%, #4d6a2f 45%, #3d5b26 70%, #2f4a20 100%); }
  .hero-photo { position: absolute; inset: 0; }
  .hero-title { position: absolute; left: 109px; top: 490px; font-family: "Montserrat", Arial, sans-serif;
    font-weight: 800; font-style: italic; font-size: 62px; color: var(--white); letter-spacing: 1px; line-height: 1; }
  .slider-dots { position: absolute; top: 640px; left: 0; width: 1200px; height: 12px; }
  .slider-dot { position: absolute; width: 10px; height: 10px; border-radius: 50%; background: rgba(120,120,120,0.6); }
  .slider-dot.is-active { width: 12px; height: 12px; background: var(--red); top: -1px; }

  .services { position: absolute; left: 0; top: 681px; width: 1200px; height: 197px; display: flex; }
  .service-tile { position: relative; width: 300px; height: 197px; }
  .service-tile.signage { background: linear-gradient(160deg, #2c3340, #262626 60%, #1f1f1f); }
  .service-tile.printing { background: linear-gradient(160deg, #3a2020, #2a2a33 55%, #1f1f22); }
  .service-tile.apparel { background: linear-gradient(160deg, #23293a, #2c2c2c 55%, #232323); }
  .service-tile.promotional { background: linear-gradient(160deg, #3a2a24, #2e2622 55%, #222); }
  .service-label { position: absolute; left: 0; top: 65px; width: 300px; text-align: center; }
  .service-rule { display: block; width: 120px; height: 1px; background: rgba(255,255,255,0.25); margin: 0 auto; }
  .service-name { display: block; padding: 21px 0 19px; font-family: "Montserrat", Arial, sans-serif; font-weight: 600; font-size: 16px; color: var(--white); text-transform: uppercase; line-height: 26px; }

  .site-footer { position: absolute; left: 0; top: 878px; width: 1200px; height: 159px; background: var(--charcoal); }
  .social { position: absolute; top: 41px; width: 29px; height: 29px; border-radius: 50%; }
  .social.s1 { left: 111px; background: #3b5998; }
  .social.s2 { left: 145px; background: #1da1f2; }
  .social.s3 { left: 179px; background: #e62117; }
  .social.s4 { left: 212px; background: #0e76a8; }
  .social.s5 { left: 247px; background: #dd4b39; }
  .copyright { position: absolute; left: 111px; top: 103px; font-size: 11.5px; color: var(--link-grey); }
  .footer-divider { position: absolute; left: 465px; top: 37px; width: 1px; height: 83px; background: #333; }
  .footer-links { position: absolute; list-style: none; top: 40px; }
  .footer-links li { position: relative; height: 31px; padding-left: 11px; font-size: 11.5px; color: var(--link-grey); line-height: 16px; }
  .footer-links li::before { content: ""; position: absolute; left: 0; top: 4px; border-left: 4px solid var(--red); border-top: 4px solid transparent; border-bottom: 4px solid transparent; }
  .col-a { left: 575px; } .col-b { left: 748px; } .col-c { left: 920px; }
</style>
</head>
<body>
  <header class="site-header">
    <div class="brand">
      <div class="brand-row"><span class="brand-dot"></span><span class="brand-name">Vexo-Marks</span></div>
      <div class="brand-tagline">Print Anything.</div>
    </div>
  </header>

  <nav class="main-nav">
    <div class="nav-active"></div>
    <span class="nav-item is-current" style="left:166px">Home</span>
    <span class="nav-item" style="left:277px">Signage</span>
    <span class="nav-item" style="left:393px">Printing</span>
    <span class="nav-item" style="left:501px">Design</span>
    <span class="nav-item" style="left:623px">Promotional</span>
    <span class="nav-item" style="left:759px">Apparel</span>
    <span class="nav-item" style="left:885px">About Us</span>
    <span class="nav-item" style="left:1018px">Contact Us</span>
  </nav>

  <section class="hero">
    <div class="hero-photo" role="img" aria-label="Photo of printed vinyl banners hung along a chain-link fence beside a grass field and cornfield under a blue sky"></div>
  </section>
  <h1 class="hero-title">PRINT ANYTHING</h1>
  <div class="slider-dots">
    <span class="slider-dot" style="left:558px"></span>
    <span class="slider-dot" style="left:581px"></span>
    <span class="slider-dot is-active" style="left:606px"></span>
  </div>

  <section class="services">
    <div class="service-tile signage" role="img" aria-label="Dark-toned photo of an outdoor monument sign">
      <div class="service-label"><span class="service-rule"></span><span class="service-name">Signage</span><span class="service-rule"></span></div>
    </div>
    <div class="service-tile printing" role="img" aria-label="Dark-toned photo of a storefront with printed window graphics">
      <div class="service-label"><span class="service-rule"></span><span class="service-name">Printing</span><span class="service-rule"></span></div>
    </div>
    <div class="service-tile apparel" role="img" aria-label="Dark-toned photo of a shop building entrance">
      <div class="service-label"><span class="service-rule"></span><span class="service-name">Apparel</span><span class="service-rule"></span></div>
    </div>
    <div class="service-tile promotional" role="img" aria-label="Dark-toned photo of a hanging oval shop sign on a brick wall">
      <div class="service-label"><span class="service-rule"></span><span class="service-name">Promotional Products</span><span class="service-rule"></span></div>
    </div>
  </section>

  <footer class="site-footer">
    <span class="social s1"></span><span class="social s2"></span><span class="social s3"></span><span class="social s4"></span><span class="social s5"></span>
    <p class="copyright">Copyright © 2016 Vexo-Marks. All Right Reserved.</p>
    <div class="footer-divider"></div>
    <ul class="footer-links col-a"><li>Signage</li><li>Printing</li><li>Design</li></ul>
    <ul class="footer-links col-b"><li>Promotional</li><li>Apparel</li><li>About Us</li></ul>
    <ul class="footer-links col-c"><li>Contact Us</li><li>Privacy Policy</li><li>Sitemap</li></ul>
  </footer>
</body>
</html>
```